Modern Billboard Ad for Criminal Defense Firm

10.5 x 36 We're looking for something to set us apart from the local competition. Looking for sleek and modern. We're a mid-sized firm in a small market city. We want to give the artist room to be creative on this one.
Thanks

Target Market(s)

Adult clients who have been charged with a crime/DWI

Industry/Entity Type

legal

Font styles to use
Serif
Sans Serif

Requirements
Must have
• Needs to have the firm name in large lettering. Law Offices of Martin G Ashby. “PLLC” does not have to be included. Phone number of (555) 318-4092 should be included but not the main focus.
Nice to have
• A call to action or something similar. “Don’t go it alone, call today.”, “ Arrested?”

```html
<!DOCTYPE html>
<html lang="en">
<head>
<meta charset="UTF-8">
<title>Martin G Ashby – Billboard</title>
<link rel="stylesheet" href="https://fonts.googleapis.com/css2?family=Cinzel:wght@400;500&family=Poppins:wght@500;800&display=swap">
<style>
  :root {
    --page: #ffffff;
    --firm-blue: #0a5096;
    --panel: #eef0f3;
    --white: #ffffff;
    --navy: #1c3f78;
    --photo-light: #b9b9b9;
    --photo-dark: #3e3e3e;
    --badge-blue: #2ea8e0;
    --badge-dark: #1d1d1f;
  }
  html, body {
    margin: 0;
    padding: 0;
    width: 1173px;
    height: 1200px;
    overflow: hidden;
    background: var(--page);
  }
  .billboard {
    position: absolute;
    left: 36px;
    top: 440px;
    width: 1100px;
    height: 321px;
    display: flex;
    box-shadow: 0 18px 50px rgba(0,0,0,0.22);
  }
  .billboard__main {
    position: relative;
    width: 914px;
    height: 100%;
    background: var(--firm-blue);
    overflow: hidden;
  }
  .attorney-photo {
    position: absolute;
    left: 0;
    top: 12px;
    width: 248px;
    height: 309px;
    background: linear-gradient(160deg, var(--photo-light) 0%, #7d7d7d 45%, var(--photo-dark) 100%);
    border-radius: 60px 90px 0 0;
  }
  .firm-name {
    position: absolute;
    left: 248px;
    right: 0;
    top: 50px;
    margin: 0;
    text-align: center;
    color: var(--white);
    font-family: 'Cinzel', serif;
    font-weight: 400;
    line-height: 1;
  }
  .firm-name__lead {
    display: block;
    font-size: 56px;
    letter-spacing: 3px;
  }
  .firm-name__attorney {
    display: block;
    font-size: 64px;
    letter-spacing: 1px;
    margin-top: 8px;
  }
  .cta {
    position: absolute;
    left: 248px;
    right: 0;
    top: 218px;
    text-align: center;
    color: var(--white);
    font-family: 'Poppins', sans-serif;
  }
  .cta__headline {
    display: block;
    font-weight: 800;
    font-size: 46px;
    line-height: 1;
    letter-spacing: -1px;
  }
  .cta__phone {
    display: block;
    font-weight: 500;
    font-size: 22px;
    margin-top: 4px;
  }
  .billboard__side {
    width: 186px;
    height: 100%;
    background: var(--panel);
    display: flex;
    flex-direction: column;
    align-items: center;
  }
  .firm-mark {
    margin-top: 58px;
    display: flex;
    flex-direction: column;
    align-items: center;
    gap: 10px;
    font-family: 'Cinzel', serif;
    font-weight: 500;
    font-size: 15px;
    letter-spacing: 1.5px;
    color: var(--navy);
  }
  .firm-mark__dot {
    width: 34px;
    height: 34px;
    border-radius: 50%;
    background: var(--navy);
  }
  .award-badge {
    margin-top: 44px;
  }
</style>
</head>
<body>
  <section class="billboard">
    <div class="billboard__main">
      <div class="attorney-photo" role="img" aria-label="Black and white portrait of the attorney in a vest and tie, holding a jacket over his shoulder"></div>
      <h1 class="firm-name">
        <span class="firm-name__lead">Law Offices of</span>
        <span class="firm-name__attorney">Martin G Ashby.</span>
      </h1>
      <p class="cta">
        <span class="cta__headline">ARRESTED?</span>
        <span class="cta__phone">(555) 318-4092</span>
      </p>
    </div>
    <aside class="billboard__side">
      <div class="firm-mark">
        <span class="firm-mark__dot"></span>
        <span class="firm-mark__name">MARTIN G ASHBY</span>
      </div>
      <svg class="award-badge" width="76" height="104" viewBox="0 0 76 104" role="img" aria-label="Community award badge">
        <rect x="0" y="0" width="76" height="104" fill="var(--badge-blue)"/>
        <rect x="4" y="22" width="68" height="66" fill="var(--badge-dark)"/>
      </svg>
    </aside>
  </section>
</body>
</html>
```